Modern, eye catching eliquid bottle label. 1.5 x 2.75

We need a label design for our e-juice bottles. The labels to be printed are 1.5 inches in height and 2.75 inches in width. We are looking to include our website (www.quillbrookmistparlor.com) and our phone number of 2 different shops. The most prominent thing needs to be our logo(attached .pdf and jpeg). We will need 2 spots that we can edit on an ongoing basis for nicotine strength and the flavor. We want something simplistic but eye-catching. Our colors are Purple, Red, and Orange. We would also like our website fairly prominent as well.

Target Market(s)

18-45 vapers and e-cigarette users

Font styles to use
Serif

Colors
6b449b
f78e1f
ec1f27
ffffff
000000

Requirements
Must have
• eye catching
• "Quillbrook Mist" must be LARGE
• phone number
• website
• areas for flavor name and nicotine strength
• orange, purple, black and red
Nice to have
• clean, abstract vectors
• "corporate look"
• think of a JUNO FIZZ can, you immediately know what your'e looking at.
• Our V in vapor is our go to logo
Should not have
• no grunge effects
• no round shapes

```html
<!DOCTYPE html>
<html lang="en">
<head>
<meta charset="utf-8">
<title>Quillbrook Mist – E-liquid Bottle Labels</title>
<link rel="stylesheet" href="https://fonts.googleapis.com/css2?family=Arimo:wght@400;700&display=swap">
<style>
  :root {
    --canvas-grey: #808080;
    --label-black: #000000;
    --brand-purple: #6b449b;
    --brand-orange: #f78e1f;
    --brand-red: #ec1f27;
    --text-orange: #f4a020;
    --text-white: #ffffff;
  }
  * { margin: 0; padding: 0; box-sizing: border-box; }
  html, body {
    width: 1200px;
    height: 1000px;
    overflow: hidden;
    background: var(--canvas-grey);
    font-family: "Arimo", Arial, sans-serif;
  }
  .canvas {
    position: relative;
    width: 1200px;
    height: 1000px;
  }
  .label {
    position: absolute;
    left: 333px;
    width: 534px;
    height: 291px;
    overflow: hidden;
    background: var(--label-black);
  }
  .label--plain { top: 164px; }
  .label--glow { top: 546px; }

  .label__backdrop {
    position: absolute;
    inset: 0;
  }
  .label--plain .label__backdrop {
    background:
      radial-gradient(ellipse 60% 28% at 45% 45%, rgba(120,120,120,0.35), transparent 70%),
      radial-gradient(ellipse 70% 22% at 70% 62%, rgba(90,90,90,0.3), transparent 70%),
      var(--label-black);
  }
  .label--glow .label__backdrop {
    background:
      radial-gradient(ellipse 30% 8% at 25% 5%, rgba(247,142,31,0.55), transparent 75%),
      radial-gradient(ellipse 20% 6% at 90% 30%, rgba(247,142,31,0.5), transparent 75%),
      radial-gradient(ellipse 35% 7% at 12% 72%, rgba(236,90,31,0.55), transparent 75%),
      radial-gradient(ellipse 30% 7% at 85% 58%, rgba(247,142,31,0.5), transparent 75%),
      radial-gradient(ellipse 30% 6% at 55% 78%, rgba(236,90,31,0.45), transparent 75%),
      radial-gradient(ellipse 60% 28% at 45% 45%, rgba(120,120,120,0.3), transparent 70%),
      var(--label-black);
  }

  .label__brand {
    position: absolute;
    left: 0;
    right: 0;
    top: 80px;
    text-align: center;
    font-size: 40px;
    font-weight: 400;
    color: var(--brand-purple);
    letter-spacing: 0.5px;
  }
  .label__flavour-caption {
    position: absolute;
    left: 0;
    right: 0;
    top: 145px;
    text-align: center;
    font-size: 18px;
    letter-spacing: 0.5px;
    color: var(--text-orange);
  }
  .label__flavour-name {
    position: absolute;
    left: 0;
    right: 0;
    top: 170px;
    text-align: center;
    font-size: 21px;
    font-weight: 700;
    letter-spacing: 1.5px;
    color: var(--brand-orange);
  }
  .label__nicotine {
    position: absolute;
    right: 14px;
    top: 199px;
    text-align: right;
    color: var(--text-white);
  }
  .label__nicotine-caption {
    font-size: 12px;
    letter-spacing: 0.6px;
  }
  .label__nicotine-value {
    font-size: 21px;
    letter-spacing: 1px;
    margin-top: 1px;
  }
  .label__phone {
    position: absolute;
    left: 0;
    right: 0;
    top: 242px;
    padding-left: 6px;
    text-align: center;
    font-size: 15px;
    letter-spacing: 1px;
    color: var(--text-orange);
  }
  .label__website {
    position: absolute;
    left: 0;
    right: 0;
    top: 263px;
    text-align: center;
    font-size: 16px;
    letter-spacing: 1.1px;
    color: var(--text-orange);
  }
</style>
</head>
<body>
<main class="canvas">

  <section class="label label--plain">
    <div class="label__backdrop" role="img" aria-label="Soft grey smoke wave on black background"></div>
    <p class="label__brand">Quillbrook Mist</p>
    <p class="label__flavour-caption">Flavour</p>
    <p class="label__flavour-name">AFTERGLOW</p>
    <div class="label__nicotine">
      <p class="label__nicotine-caption">Nicotine Strength:</p>
      <p class="label__nicotine-value">6 mg</p>
    </div>
    <p class="label__phone">Ph: 555-014-2277</p>
    <p class="label__website">www.quillbrookmistparlor.com</p>
  </section>

  <section class="label label--glow">
    <div class="label__backdrop" role="img" aria-label="Grey smoke wave with glowing orange light streaks on black background"></div>
    <p class="label__brand">Quillbrook Mist</p>
    <p class="label__flavour-caption">Flavour</p>
    <p class="label__flavour-name">AFTERGLOW</p>
    <div class="label__nicotine">
      <p class="label__nicotine-caption">Nicotine Strength:</p>
      <p class="label__nicotine-value">6 mg</p>
    </div>
    <p class="label__phone">Ph: 555-014-2277</p>
    <p class="label__website">www.quillbrookmistparlor.com</p>
  </section>

</main>
</body>
</html>
```